Rebranding and redesign of our website AND logo

Just to be CLEAR. This projects is for a website bundled with a Logo. Please submit logo and site. Combined with design or logo separate. Thank you!
--
We need a new website design and logo design for our web agency in Belgium. We develop websites and ecommerce sites. For our designs we like to outsource it to freelancers or in this case PixelBazaar.
We want the new look to have a not-too corporate look and feel. We want the site to communicate personal connection, trust/transparency and professionalism. It can be a bit 'out of the box' as well.

We already have a moodboard we mainly used for the Logo brainstorms: https://www.snapquilt.com/rvanost7734/korvel/

And the current website is:
https://studio-korvel.be
+ colors
+ not to cluttered, good whitespace
+ balanced rounded design elements
- missing consistency
- its all a bit too 'foaty' on the white canvas. Missing some connection between the different blocks
- logo

We do not dislike the current colors of the website as these are not very commonly used in web but if you have another vision on the colors in the logo or design we are open for this.

As reference of what direction we want to take the site
what we like + or dislike - on the 2 following templates:
https://flex.fennickhale.com/brightmoss/
+ fonts
+ whitespacing
+ layout
+ minimalistic
- footer to minimalistic (needs more info)
- no color

https://demo.fennickhale.com/pelatown/
+ layout
+ creative play with fonts (subtitle inside the title of the blocks)
+ whitespace
+ footer
- hero with just a title and no extra info above the fold
Updates

Some designers got feedback on their designs. We are just giving them time for their changes to be made. Do not submit anything new unless we gave feedback on an already submitted design. (However a completely different style in line with the designs from the design brief are accepted.)

Target Market(s)

ecommerce

Industry/Entity Type

internet, digital, tech

Number of Pages Required

3 page

Font styles to use
Sans Serif

Colors

Designer to choose colors to be used in the design.

Requirements
Must have
• Minimalistic, modern, clean, in line with the snapquilt moodboard, white or light backgrounds
Nice to have
• a few creative elements that make the design pop/stand out
Should not have
• shadows, gradients, large dark/black color backgrounds.

```html
<!DOCTYPE html>
<html lang="nl">
<head>
<meta charset="utf-8">
<title>Korvel – Web Agency</title>
<link rel="stylesheet" href="https://fonts.googleapis.com/css2?family=Montserrat:wght@300;400;500;600;700&display=swap">
<style>
:root{
  --backdrop:#f1e1fe;
  --ink:#1d1b22;
  --muted:#6d6a74;
  --violet:#9a00ff;
  --pink:#e3306e;
  --night:#3b2256;
  --plum-a:#3a1a5e;
  --plum-b:#5b2a8c;
  --tile:#3f1e66;
  --support:#121115;
  --foot:#40306c;
  --white:#ffffff;
}
*{box-sizing:border-box;margin:0;padding:0}
html,body{width:1200px;height:1200px;overflow:hidden;background:var(--backdrop);font-family:'Montserrat',sans-serif;color:var(--ink)}
.page{position:absolute;left:453px;top:38px;width:584px;height:1820px;transform:scale(.6211);transform-origin:0 0;background:var(--white);box-shadow:0 0 2px rgba(0,0,0,.25);overflow:hidden}
.abs{position:absolute}

/* header + hero */
.hero{position:absolute;left:0;top:0;width:584px;height:328px;background:linear-gradient(160deg,#4d2c68 0%,#3e2358 55%,#2f1a45 100%)}
.nav{position:absolute;left:0;top:0;width:584px;height:56px;background:rgba(50,28,74,.85)}
.brand{position:absolute;left:50px;top:14px;display:flex;align-items:center;gap:6px;color:var(--white);font-weight:600;font-size:19px;letter-spacing:.5px}
.brand .dot{width:30px;height:22px;background:var(--violet);border-radius:4px}
.menu{position:absolute;left:194px;top:20px;display:flex;gap:21px;font-size:7.5px;color:#e8e0f2}
.menu span:first-child{border-bottom:1px solid var(--pink);padding-bottom:3px}
.help-btn{position:absolute;left:414px;top:16px;width:122px;height:22px;border-radius:11px;background:var(--pink);color:var(--white);font-size:7.5px;font-weight:700;display:flex;align-items:center;justify-content:center}
.hero-title{position:absolute;left:0;top:100px;width:584px;text-align:center;color:var(--white);font-weight:700;font-size:25px;line-height:32px}
.hero-title em{font-style:normal;color:var(--violet)}
.hero-tag{position:absolute;left:0;top:173px;width:584px;text-align:center;color:var(--violet);font-size:12px}
.hero-copy{position:absolute;left:82px;top:190px;width:420px;text-align:center;color:#eee6f6;font-size:7.2px;line-height:11.5px}
.btn{position:absolute;height:26px;border-radius:13px;font-size:8.5px;font-weight:700;display:flex;align-items:center;justify-content:center;color:var(--white)}
.btn-pink{background:var(--pink)}
.btn-line{border:1.2px solid var(--white)}

/* feature cards */
.feature{position:absolute;top:302px;width:162px;height:131px;background:var(--white);padding:16px 12px 0;box-shadow:0 1px 3px rgba(0,0,0,.12)}
.feature h3{font-size:9px;font-weight:500;line-height:11px;margin-top:6px}
.feature p{font-size:6.8px;line-height:9.5px;color:var(--muted);margin-top:14px}
.feature.is-active{background:var(--violet);color:var(--white)}
.feature.is-active p{color:#f0dcff}

/* cases */
.eyebrow{font-size:8px;color:var(--violet)}
.section-title{font-weight:400;font-size:24px;line-height:26px}
.case{position:absolute;left:292px;width:246px}
.case .num{display:flex;align-items:center;gap:4px;font-size:13px}
.case .num i{flex:1;height:1px;background:#bdbac2}
.case h4{font-size:10px;font-weight:400;line-height:10px;margin-top:11px}
.case p{font-size:7px;line-height:11.8px;color:var(--muted);margin-top:15px}
.case .more{font-size:7.5px;color:var(--violet);margin-top:6px;display:flex;align-items:center;gap:6px}
.btn-outline-dark{position:absolute;left:51px;top:559px;width:122px;height:28px;border:1.2px solid var(--ink);border-radius:14px;font-size:8.5px;display:flex;align-items:center;justify-content:center}

/* partner section */
.partner{position:absolute;left:0;top:760px;width:584px;height:382px;background:linear-gradient(150deg,var(--plum-a),var(--plum-b) 60%,#4a2278)}
.partner .kicker{position:absolute;top:30px;width:584px;text-align:center;color:#eadcf8;font-size:10.5px}
.partner h2{position:absolute;top:50px;width:584px;text-align:center;color:var(--white);font-size:15.5px;font-weight:700}
.partner .rule{position:absolute;left:90px;top:85px;width:402px;height:1px;background:var(--pink)}
.tile{position:absolute;width:128px;height:112px;background:var(--tile);border-radius:6px;text-align:center;color:var(--white);padding-top:14px}
.tile h5{font-size:8.5px;font-weight:700;line-height:10px;margin-top:4px}
.tile p{font-size:6.3px;line-height:10.5px;color:#d8cbe6;margin:6px 6px 0}
.tile svg{display:block;margin:0 auto}

/* solutions */
.solution{position:absolute;top:1234px;width:236px;height:196px;border-radius:4px;overflow:hidden}
.solution .shot{position:absolute;inset:0}
.solution h4{position:absolute;top:26px;width:236px;text-align:center;color:var(--white);font-size:11px;font-weight:700}
.solution h4 em{font-style:normal;color:var(--pink)}
.solution .panel{position:absolute;left:40px;top:48px;width:158px;height:128px;background:var(--white);border-radius:6px;padding:16px 10px 0 12px}
.solution ul{list-style:none;font-size:6.2px;line-height:15.5px;color:#444}
.solution li::before{content:"•";margin-right:5px}
.solution .cta{position:absolute;left:17px;bottom:14px;width:124px;height:24px;border-radius:12px;background:var(--pink);color:var(--white);font-size:7.5px;display:flex;align-items:center;justify-content:center}
.clients{position:absolute;left:46px;top:1476px;width:492px;display:flex;justify-content:space-between}
.client{width:90px;height:38px;background:var(--white);box-shadow:0 1px 3px rgba(0,0,0,.15);display:flex;align-items:center;justify-content:center;font-size:15px;font-weight:600;color:#333}

/* support + footer */
.support{position:absolute;left:0;top:1554px;width:584px;height:101px;background:var(--support);color:var(--white);text-align:center}
.support h6{font-size:8px;font-weight:400;margin-top:14px}
.support .sub{font-size:4.5px;color:#aaa;margin-top:4px}
.contact{position:absolute;top:48px;width:110px;font-size:4.6px;line-height:6.5px;color:#ddd}
.footer{position:absolute;left:0;top:1655px;width:584px;height:165px;background:var(--foot);color:var(--white);text-align:center}
.footer .big{position:absolute;left:0;top:14px;width:584px;display:flex;justify-content:center;align-items:center;gap:12px;font-size:38px;font-weight:600;letter-spacing:1px}
.footer .big i{width:70px;height:46px;background:var(--violet);border-radius:8px}
.footer .rule{position:absolute;left:4px;top:78px;width:576px;height:1px;background:#7b6ca0}
.socials{position:absolute;top:90px;width:584px;display:flex;justify-content:center;gap:26px;font-size:6px}
.socials span{display:flex;align-items:center;gap:3px}
.socials span::before{content:"";width:8px;height:8px;border-radius:50%;background:var(--white)}
.legal{position:absolute;top:110px;width:584px;font-size:5.6px;line-height:10px;color:#e6def2}
.legal a{color:#c79bff;text-decoration:none;margin-left:5px}
</style>
</head>
<body>
<main class="page">

  <section class="hero" role="img" aria-label="Dark violet photo of people working at laptops"></section>
  <header class="nav">
    <div class="brand"><span class="dot"></span>KORVEL</div>
    <nav class="menu"><span>Oplossingen</span><span>Cases</span><span>Over ons</span><span>Contact</span></nav>
    <div class="help-btn">Je PressKit hulplijn</div>
  </header>
  <h1 class="hero-title">De Laatste <em>Web Agency</em> Waarmee<br>Je Nog in Zee Zal Gaan</h1>
  <div class="hero-tag">Daar gaan wij voor!</div>
  <p class="hero-copy">Wij bieden e-commerce en website oplossingen met een doordachte strategie die ook haalbaar is voor je onderneming. Bij Studio Korvel zijn we gepassioneerd over wat we doen, en we zijn toegewijd om een persoonlijke en de best mogelijke service aan onze klanten te leveren.</p>
  <div class="btn btn-pink" style="left:192px;top:243px;width:92px">Lees meer</div>
  <div class="btn btn-line" style="left:301px;top:243px;width:92px">Contacteer ons</div>

  <article class="feature" style="left:46px">
    <svg width="22" height="20" viewBox="0 0 22 20" fill="none" stroke="#9a00ff" stroke-width="1.2"><path d="M1 2h3l3 11h11l2-8H6"/><circle cx="9" cy="17" r="1.5"/><circle cx="16" cy="17" r="1.5"/></svg>
    <h3>Je website en e-commerce platform</h3>
    <p>Verkoop je producten, je diensten of jezelf… in stijl. PressKit of Shopvane, dat is ons ding!</p>
  </article>
  <article class="feature" style="left:211px">
    <svg width="16" height="22" viewBox="0 0 16 22" fill="none" stroke="#9a00ff" stroke-width="1.2"><circle cx="8" cy="8" r="6.5"/><path d="M5 15v3h6v-3M6 20h4M8 14V8M6 8l2 2 2-2"/></svg>
    <h3>Je website lanceren met een strategie</h3>
    <p>Digitale strategie voor je website en sociale media. Van a tot z de relatie met je klanten digitaal verbeteren.</p>
  </article>
  <article class="feature is-active" style="left:374px;padding-left:19px">
    <svg width="30" height="18" viewBox="0 0 30 18" fill="none" stroke="#fff" stroke-width="1.2"><path d="M1 9h27M20 2l8 7-8 7"/></svg>
    <h3>Je organisatie digitale stappen vooruit laten zetten</h3>
    <p>Ook achter de schermen helpen we je op weg. Je interne werking automatiseren, verbeterde dienstverlening en efficiënter samenwerken.</p>
  </article>

  <div class="abs eyebrow" style="left:50px;top:477px">Cases</div>
  <h2 class="abs section-title" style="left:49px;top:491px">Recente<br>successverhalen</h2>
  <div class="btn-outline-dark">Onze realisaties</div>

  <article class="case" style="top:476px">
    <div class="num">01<i></i></div>
    <h4>7 Uitdagingen in online verkoop (en hoe we het bij Bramwick aanpakten)</h4>
    <p>Een flexibele webshop die kan groeien. Optimaal nieuwe klanten online bereiken en maximale efficiëntie intern. Ontdek de 7 uitdagingen bij online verkoop waar Bramwick voor stond, en hoe we het aanpakten.</p>
    <div class="more">Lees meer <svg width="16" height="8" viewBox="0 0 16 8" fill="none" stroke="#9a00ff"><path d="M0 4h15M11 1l4 3-4 3"/></svg></div>
  </article>
  <article class="case" style="top:616px">
    <div class="num">02<i></i></div>
    <h4>Integratie van verkoopskanalen: Marivo</h4>
    <p>Naadloze integratie van de webshop met een groot assortiment op verschillende verkoopkanalen en met geautomatiseerde administratie</p>
    <div class="more">Lees meer <svg width="16" height="8" viewBox="0 0 16 8" fill="none" stroke="#9a00ff"><path d="M0 4h15M11 1l4 3-4 3"/></svg></div>
  </article>

  <section class="partner">
    <div class="kicker">Op ons kan je rekenen</div>
    <h2>Je website partner voor succes</h2>
    <div class="rule"></div>

    <div class="tile" style="left:90px;top:106px"><svg width="32" height="14" viewBox="0 0 32 14" fill="none" stroke="#e3306e" stroke-width="1.5"><path d="M1 7h28M18 1l7 6-7 6M23 1l7 6-7 6"/></svg><h5>Snel resultaat</h5><p>Onze tools laten ons toe om snel op te starten, snel te schakelen en is snel bij te sturen.</p></div>
    <div class="tile" style="left:228px;top:106px;padding-top:6px"><svg width="30" height="24" viewBox="0 0 30 24" fill="#e3306e"><circle cx="11" cy="15" r="6"/><circle cx="22" cy="7" r="4.5"/><circle cx="11" cy="15" r="2" fill="#3f1e66"/><circle cx="22" cy="7" r="1.5" fill="#3f1e66"/></svg><h5>E-commerce<br>oplossingen</h5><p>Wij bieden diverse oplossingen voor kleine en grote ondernemingen.</p></div>
    <div class="tile" style="left:366px;top:106px;padding-top:8px"><svg width="22" height="22" viewBox="0 0 22 22" fill="none" stroke="#e3306e" stroke-width="2.4"><path d="M3 19L17 5M5 3l14 14"/></svg><h5>Zelf in controle</h5><p>Je site zelf aanpassen en uitbreiden. Ja dat kan!</p></div>

    <div class="tile" style="left:90px;top:232px;padding-top:6px"><svg width="20" height="26" viewBox="0 0 20 26" fill="#e3306e"><path d="M10 2c5 3 6 9 2 13l1 9H7l1-9C4 11 5 5 10 2z"/></svg><h5>Opleidingen op maat</h5><p>We leren je de knepen van het vak en neem de touwtjes zelf in handen.</p></div>
    <div class="tile" style="left:228px;top:232px;padding-top:10px"><svg width="26" height="18" viewBox="0 0 26 18" fill="#e3306e"><circle cx="8" cy="5" r="4"/><circle cx="18" cy="5" r="4"/><path d="M1 17c0-5 3-7 7-7s6 2 6 7zM13 17c0-5 2-7 5-7s7 2 7 7z"/></svg><h5>Wij flankeren waar nodig</h5><p>Laat je team doen waar het goed in is. Wij doen de rest wel.</p></div>
    <div class="tile" style="left:366px;top:232px;padding-top:6px"><svg width="24" height="24" viewBox="0 0 24 24" fill="#e3306e"><path d="M6 22h12v-3H6zM8 18h8l-1-7 3-3-5-5-5 3 2 3-3 2z"/></svg><h5>Strategie en advies</h5><p>Wij verkopen geen mooie verhalen. Wij geven je haalbare strategie en advies op maat.</p></div>
  </section>

  <div class="abs eyebrow" style="left:0;top:1162px;width:584px;text-align:center">Technologie</div>
  <h2 class="abs section-title" style="left:0;top:1188px;width:584px;text-align:center">Onze Weboplossingen</h2>

  <article class="solution" style="left:48px">
    <div class="shot" role="img" aria-label="Dark photo of a desk with laptop and plant" style="background:linear-gradient(135deg,#555a63,#2c2f36 60%,#4a4f55)"></div>
    <h4>Je <em>website</em> in PressKit</h4>
    <div class="panel">
      <ul><li>Top marketing platform</li><li>Gebruiksvriendelijk</li><li>Snel en eenvoudig uitbreidbaar</li><li>Ook ideaal voor startende webshops</li></ul>
      <div class="cta">Onze PressKit oplossing</div>
    </div>
  </article>
  <article class="solution" style="left:300px">
    <div class="shot" role="img" aria-label="Dark photo of a laptop with online payment screen" style="background:linear-gradient(135deg,#3a3e46,#22252b 60%,#5a5f68)"></div>
    <h4>Je <em>webshop</em> in Shopvane</h4>
    <div class="panel">
      <ul><li>Multi-channel commerce-ervaring</li><li>Voor zowel B2B- en B2C</li><li>Flexibel en uitbreidbaar handelsplatform</li><li>Schaalbaar en veilig</li></ul>
      <div class="cta">Onze Shopvane oplossing</div>
    </div>
  </article>

  <div class="clients">
    <div class="client">Bramwick</div><div class="client">Halvorn</div><div class="client">Quillo</div><div class="client">Trevant</div><div class="client">Lumora</div>
  </div>

  <section class="support">
    <h6>Our Dedicated Support</h6>
    <div class="sub">We kijken ernaar uit om je te helpen je online doelen te bereiken.</div>
    <div class="contact" style="left:104px"><svg width="9" height="9" viewBox="0 0 10 10" fill="#fff"><path d="M2 0l2 2-1 2 3 3 2-1 2 2-2 2C4 10 0 6 0 2z"/></svg><br>Call Us<br>+32 470 55 21 08<br>Mon-Fri 9AM-5PM</div>
    <div class="contact" style="left:237px"><svg width="9" height="7" viewBox="0 0 10 8" fill="#fff"><rect width="10" height="8" rx="1"/><path d="M0 0l5 4 5-4" stroke="#121115" fill="none"/></svg><br>Email Us<br>hallo@studio-korvel.be<br>Vlierstraat 12</div>
    <div class="contact" style="left:367px"><svg width="9" height="9" viewBox="0 0 10 10"><circle cx="5" cy="5" r="5" fill="#fff"/></svg><br>Live Chat<br>Available on our website<br>Mon-Fri 8AM-6PM</div>
  </section>

  <footer class="footer">
    <div class="big"><i></i>KORVEL</div>
    <div class="rule"></div>
    <div class="socials"><span>Chat</span><span>Foto</span><span>Feed</span><span>Net</span></div>
    <div class="legal">Zet je zaak op de kaart<br>Als je op zoek bent naar een digital agency die je snel kan helpen je onderneming naar het volgende niveau te tillen, neem dan vandaag nog contact met ons op.<br>We kijken ernaar uit om je te helpen je online doelen te bereiken.<a>Privacy Policy</a><a>Terms of Use</a><a>Cookie Policy</a></div>
  </footer>

</main>
</body>
</html>
```